Business Card Design

New Homes
Renovations/Additions
Building Maintenance
Design
Council Approvals
Estimates
Project and Construction Management

The back of the card should only contain my logo which is attached and under the logo have written velora & velora constructions.

Industry/Entity Type

Business

Contact Information for Business Card

Company Name: Velora & Velora Constructions Pty Ltd
BLD 641372
ABN: 52 907 314 286
Position: Director
Name: Tavo Rilkenbar
Tel: m. 0418276354
f. (08)83926157
veloranvelora@mailnest.example

```html
<!DOCTYPE html>
<html lang="en">
<head>
<meta charset="utf-8">
<title>Velora &amp; Velora Constructions – Business Card</title>
<link rel="stylesheet" href="https://fonts.googleapis.com/css2?family=Play:wght@700&family=Arimo:wght@400&display=swap">
<style>
  :root {
    --backdrop: #8c8c8c;
    --card-dark: #3d3d3d;
    --card-light: #ffffff;
    --ink-dark: #1c1c1c;
    --ink-light: #ffffff;
    --ink-muted: #333333;
  }
  html, body {
    margin: 0;
    width: 1200px;
    height: 1000px;
    overflow: hidden;
    background: var(--backdrop);
  }
  .canvas {
    position: relative;
    width: 1200px;
    height: 1000px;
  }
  .card {
    position: absolute;
    top: 328px;
    width: 556px;
    height: 344px;
    box-shadow: 0 2px 6px rgba(0,0,0,0.35);
  }
  .card--front { left: 30px; }
  .card--back { left: 612px; }
  .card svg { display: block; }
  .name { font-family: "Play", sans-serif; font-weight: 700; font-size: 23px; letter-spacing: 1px; fill: var(--ink-light); }
  .role { font-family: "Arimo", Arial, sans-serif; font-size: 14px; fill: var(--ink-light); }
  .contact { font-family: "Arimo", Arial, sans-serif; font-size: 15px; fill: var(--ink-light); }
  .company { font-family: "Arimo", Arial, sans-serif; font-size: 14.5px; fill: var(--ink-dark); }
  .services { font-family: "Arimo", Arial, sans-serif; font-size: 14px; fill: var(--ink-muted); }
  .brand-name { font-family: "Arimo", Arial, sans-serif; font-weight: 400; font-size: 40px; fill: var(--ink-dark); }
  .brand-line { font-family: "Arimo", Arial, sans-serif; font-weight: 400; font-size: 24px; fill: var(--ink-dark); }
</style>
</head>
<body>
<main class="canvas">

  <section class="card card--front" aria-label="Business card front">
    <svg width="556" height="344" viewBox="0 0 556 344">
      <rect width="556" height="344" fill="var(--card-dark)"/>
      <path d="M0 256 Q278 150 556 258 L556 344 L0 344 Z" fill="var(--card-light)"/>

      <text class="name" x="276" y="57">Tavo Rilkenbar</text>
      <text class="role" x="276" y="80">Director</text>

      <g class="contact-icons" fill="var(--ink-light)">
        <rect x="45" y="120" width="7" height="12" rx="1.5"/>
        <rect x="46.5" y="122" width="4" height="4" fill="var(--card-dark)"/>
        <path d="M52 144 q-1 8 -7 11 l-1.5 -2 q4 -3 5 -8 Z"/>
        <rect x="45" y="174" width="12" height="8"/>
        <path d="M45 174 L51 179 L57 174" stroke="var(--card-dark)" stroke-width="1.2" fill="none"/>
      </g>
      <text class="contact" x="70" y="132">0418276354</text>
      <text class="contact" x="70" y="157">(08)83926157</text>
      <text class="contact" x="70" y="183">veloranvelora@mailnest.example</text>

      <text class="company" x="280" y="247" text-anchor="middle">Velora &amp; Velora Constructions Pty Ltd, BLD 641372</text>
      <text class="company" x="280" y="268" text-anchor="middle">ABN: 52 907 314 286</text>
      <text class="services" x="280" y="296" text-anchor="middle">New Homes | Renovations/Additions | Building Maintenance</text>
      <text class="services" x="280" y="314" text-anchor="middle">Design | Council Approvals | Estimates | Project and Construction Management</text>
    </svg>
  </section>

  <section class="card card--back" aria-label="Business card back">
    <svg width="556" height="344" viewBox="0 0 556 344">
      <rect width="556" height="344" fill="var(--card-dark)"/>
      <ellipse cx="278" cy="175" rx="292" ry="162" fill="var(--card-light)"/>
      <text class="brand-name" x="278" y="170" text-anchor="middle">Velora &amp; Velora</text>
      <text class="brand-line" x="278" y="278" text-anchor="middle">Velora &amp; Velora Constructions</text>
    </svg>
  </section>

</main>
</body>
</html>
```